Business Card Design Project

Use our current logo. Clean design.

Industry/Entity Type

Business

Requirements
Must have
• Marisela DUCRANTE
M. Law
Managing Partner

Velotrana AG
Brunnmattweg 274
CH-3097 Liebefeld

M. +41 79 418 26 97
T. +41 31 742 19 04
F. +41 31 742 19 38

m.ducrante@velotrana.example
www.velotrana.example

```html
<!DOCTYPE html>
<html lang="en">
<head>
<meta charset="utf-8">
<title>Velotrana AG – Business Card</title>
<link rel="stylesheet" href="https://fonts.googleapis.com/css2?family=Arimo:wght@400;700&display=swap">
<style>
  :root {
    --stage: #e4e4e4;
    --card-light: #f2f2f2;
    --card-band: #e2e2e2;
    --card-dark: #7f7f7f;
    --ink: #1a1a1a;
    --ink-soft: #3a3a3a;
    --mark-faint: #ffffff;
  }
  * { box-sizing: border-box; margin: 0; padding: 0; }
  html, body {
    width: 1200px;
    height: 900px;
    overflow: hidden;
    background: var(--stage);
    font-family: "Arimo", Arial, sans-serif;
  }
  .stage {
    position: relative;
    width: 1200px;
    height: 900px;
    display: flex;
    align-items: center;
    justify-content: center;
    gap: 40px;
  }
  .card {
    position: relative;
    width: 520px;
    height: 336px;
    overflow: hidden;
    box-shadow: 0 2px 6px rgba(0, 0, 0, 0.12);
  }

  /* Contact side */
  .card--contact {
    background: var(--card-light);
  }
  .card--contact .edge-band {
    position: absolute;
    left: 0;
    top: 0;
    width: 14px;
    height: 100%;
    background: var(--card-band);
  }
  .card--contact .brand-watermark {
    position: absolute;
    right: -40px;
    top: -62px;
    font-size: 150px;
    font-weight: 400;
    letter-spacing: -2px;
    color: var(--mark-faint);
    white-space: nowrap;
    line-height: 1;
  }
  .contact-block {
    position: absolute;
    left: 38px;
    top: 96px;
    font-size: 12.5px;
    line-height: 15px;
    color: var(--ink-soft);
  }
  .contact-block .group { margin-bottom: 10px; }
  .contact-block .label {
    display: inline-block;
    width: 16px;
    font-weight: 700;
    color: var(--ink);
  }
  .contact-block .person-name {
    font-weight: 700;
    font-size: 13.5px;
    color: var(--ink);
  }

  /* Brand side */
  .card--brand {
    background: var(--card-dark);
    display: flex;
    align-items: center;
    justify-content: center;
  }
  .brand-name {
    font-size: 40px;
    font-weight: 400;
    letter-spacing: 1px;
    color: var(--ink);
  }
</style>
</head>
<body>
  <main class="stage">
    <section class="card card--contact" aria-label="Contact side">
      <div class="edge-band"></div>
      <div class="brand-watermark" aria-hidden="true">Velotrana</div>
      <div class="contact-block">
        <div class="group">
          Velotrana AG<br>
          Brunnmattweg 274<br>
          CH-3097 Liebefeld
        </div>
        <div class="group">
          <span class="label">M</span>+41 79 418 26 97<br>
          <span class="label">T</span>+41 31 742 19 04<br>
          <span class="label">F</span>+41 31 742 19 38
        </div>
        <div class="group">
          m.ducrante@velotrana.example<br>
          www.velotrana.example
        </div>
        <div class="group">
          <span class="person-name">Marisela DUCRANTE</span><br>
          M. Law<br>
          Managing Partner
        </div>
      </div>
    </section>

    <section class="card card--brand" aria-label="Brand side">
      <div class="brand-name">Velotrana</div>
    </section>
  </main>
</body>
</html>
```